BRINTEX Hardware needs a Flyer Designed

We need a flyer designed for a marketing strategy that is to be launched by BRINTEX. As it is for our hardware division, our logo should go unto the flyer. We are offering to our customers financing on items from $5000 up to $35000. Here are some key words that you may want to include; "building or revovating? you pick the job we've got the financing." The flyer should reflect some sort of home construction and should be very attractive and vibrant. On the flyer it should also state that it's "hassle-free" and; "no down payment", "no collateral", "affordable monthly payments".

Must Haves [en ]: The companies logo. Also it must state the address of the company and contact info which is; 47 Fellowby Lane Penal, Trinidad. Tel: 555-47-BRINTEX. Email must also be listed: info@brintexgroup.example.

Nice To Haves [en ]: Good quality graphics. something that is captivating and that will hold the attention of our audience.

Should Not Haves [en ]: Should not be too busy.

Requirements
Must have
• The companies logo. Also it must state the address of the company and contact info which is; 47 Fellowby Lane Marrowdale, Westerly. Tel: 555-47-BRINTEX. Email must also be listed: info@brintexgroup.example.
Nice to have
• Good quality graphics. something that is captivating and that will hold the attention of our audience.
Should not have
• Should not be too busy.

```html
<!DOCTYPE html>
<html lang="en">
<head>
<meta charset="utf-8">
<title>BRINTEX Hardware – Financing Flyer</title>
<link href="https://fonts.googleapis.com/css2?family=Lato:wght@400;700;900&family=Michroma&family=Oswald:wght@500&display=swap" rel="stylesheet">
<style>
  :root {
    --navy: #27305f;
    --red: #c1272d;
    --ink: #4a4a4a;
    --white: #ffffff;
    --paper: #eef0f4;
  }
  * { margin: 0; padding: 0; box-sizing: border-box; }
  html, body { width: 1200px; height: 900px; overflow: hidden; background: var(--white); }
  .flyer {
    position: relative;
    width: 1200px;
    height: 900px;
    background: var(--white);
    font-family: "Lato", sans-serif;
    color: var(--ink);
    overflow: hidden;
  }
  .construction-visual {
    position: absolute;
    left: 520px;
    top: 300px;
    width: 680px;
    height: 530px;
    background:
      radial-gradient(ellipse at 70% 45%, rgba(185,188,194,.9) 0%, rgba(185,188,194,0) 45%),
      radial-gradient(ellipse at 45% 70%, rgba(200,113,74,.85) 0%, rgba(200,113,74,0) 40%),
      linear-gradient(90deg, rgba(238,240,244,0) 0%, var(--paper) 35%, #e4e6ea 100%);
  }
  .offer-banner {
    position: absolute;
    left: 737px;
    top: 0;
    width: 404px;
    height: 380px;
  }
  .offer-banner svg { position: absolute; inset: 0; }
  .offer-text {
    position: absolute;
    inset: 36px 0 0 0;
    text-align: center;
    font-family: "Oswald", sans-serif;
    font-weight: 500;
    color: var(--white);
    font-size: 74px;
    line-height: 86px;
    letter-spacing: -1px;
  }
  .brand {
    position: absolute;
    left: 86px;
    top: 96px;
    width: 550px;
  }
  .brand-name {
    display: flex;
    align-items: center;
    gap: 22px;
    font-weight: 900;
    font-size: 110px;
    line-height: 1;
    color: var(--navy);
    letter-spacing: 2px;
  }
  .brand-dot {
    width: 70px; height: 70px;
    border-radius: 50%;
    background: var(--red);
    flex: none;
  }
  .brand-rule { margin-top: 22px; height: 3px; background: var(--navy); }
  .headline {
    position: absolute;
    left: 86px;
    top: 388px;
    font-family: "Michroma", sans-serif;
    color: var(--red);
    font-size: 43px;
    line-height: 56px;
    -webkit-text-stroke: 1px var(--red);
  }
  .tagline {
    position: absolute;
    left: 86px;
    top: 515px;
    font-size: 33px;
    line-height: 44px;
    color: var(--ink);
  }
  .benefits {
    position: absolute;
    left: 86px;
    top: 664px;
    list-style: none;
    font-size: 37px;
    line-height: 47px;
    color: var(--ink);
  }
  .benefits li { display: flex; align-items: center; gap: 18px; }
  .benefits svg { width: 34px; height: 30px; flex: none; }
  .social {
    position: absolute;
    right: 72px;
    top: 748px;
    display: flex;
    gap: 14px;
  }
  .social span {
    width: 52px; height: 52px;
    border-radius: 50%;
    border: 2px solid var(--red);
    background: var(--white);
  }
  .contact-bar {
    position: absolute;
    left: 0; right: 0; bottom: 0;
    height: 72px;
    background: var(--navy);
    border-top: 5px solid var(--red);
    color: var(--white);
    font-size: 26px;
    display: flex;
    align-items: center;
    padding-left: 64px;
    gap: 50px;
  }
  .contact-bar .sep { margin: 0 16px; }
</style>
</head>
<body>
<main class="flyer">
  <div class="construction-visual" role="img" aria-label="House under construction with bricks, a trowel and rolled blueprints on building plans"></div>

  <div class="offer-banner">
    <svg width="404" height="380" viewBox="0 0 404 380" aria-hidden="true">
      <polygon points="0,0 404,0 404,340 202,365 0,345" fill="var(--navy)"/>
      <polygon points="0,0 404,0 404,325 202,350 0,330" fill="var(--red)"/>
    </svg>
    <div class="offer-text">GET UP TO<br>$35,000.00<br>HASSLE-FREE</div>
  </div>

  <header class="brand">
    <div class="brand-name"><span>BRINTEX</span><span class="brand-dot"></span></div>
    <div class="brand-rule"></div>
  </header>

  <h1 class="headline">BUILDING OR<br>RENOVATING?</h1>
  <p class="tagline">You Pick the Job, We’ve<br>got the Finances!</p>

  <ul class="benefits">
    <li><svg viewBox="0 0 34 30"><rect x="2" y="6" width="22" height="20" rx="3" fill="none" stroke="var(--navy)" stroke-width="3"/><path d="M8 15 l6 6 L31 3" fill="none" stroke="var(--red)" stroke-width="4" stroke-linecap="round"/></svg>No Down-payment</li>
    <li><svg viewBox="0 0 34 30"><rect x="2" y="6" width="22" height="20" rx="3" fill="none" stroke="var(--navy)" stroke-width="3"/><path d="M8 15 l6 6 L31 3" fill="none" stroke="var(--red)" stroke-width="4" stroke-linecap="round"/></svg>No Collateral</li>
    <li><svg viewBox="0 0 34 30"><rect x="2" y="6" width="22" height="20" rx="3" fill="none" stroke="var(--navy)" stroke-width="3"/><path d="M8 15 l6 6 L31 3" fill="none" stroke="var(--red)" stroke-width="4" stroke-linecap="round"/></svg>Affordable Monthly Payments</li>
  </ul>

  <div class="social" aria-hidden="true"><span></span><span></span><span></span></div>

  <footer class="contact-bar">
    <span>47 Fellowby Lane Marrowdale, Westerly</span>
    <span>Tel: 555-47-BRINTEX.<span class="sep">|</span>info@brintexgroup.example.</span>
  </footer>
</main>
</body>
</html>
```